Tree Pruning Website

We need a website for a tree Arborist, pruning company called Hollow Ridge Groundcare. We look after all types of trees, knock down trees and prune trees. Our target market is from domestic clients to government clients and everything in between.

We would like to see the use of our main colours which are orange and green

We are not looking forward in seeing a template that we have seen before but a unique template. We have designed 5 templates ourselves and we wish for the design community to take our designs to the next level.

We have also designed a template for things that **we are not** looking for (Version 4)

To make it fair for everyone, we are also not giving out any participation payments as we have had. One winner will take all of the payment!!!

I Have attached a image of the designs and a image of a tree.

We are just looking at the PSD file been developed. We have our own team who can slice the image up into a HTML format.

Target Market(s)

Everyone who needs to cut down a tree

Industry/Entity Type

Government

Requirements
Must have
• Logo on front page
A List of our services
jQuery slider on page
Phone Number on every page

```html
<!DOCTYPE html>
<html lang="en">
<head>
<meta charset="utf-8">
<title>Hollow Ridge Groundcare</title>
<link href="https://fonts.googleapis.com/css2?family=Arimo:wght@400;700&display=swap" rel="stylesheet">
<style>
:root{
  --nav:#5f8a52;
  --nav-active:#8cb67b;
  --band:#76a564;
  --green-text:#6e9e5c;
  --rule:#a9c99b;
  --frame:#c6ddbb;
  --box-top:#cde6c0;
  --box-bottom:#79a966;
  --tab:#74a25f;
  --tab-dark:#567f46;
  --body-text:#5a5a5a;
  --dark-text:#333;
  --logo-border:#e2e2e2;
  --logo-text:#d8d8d8;
  --footer-top:#c3e0b4;
  --footer-bottom:#8dbb78;
  --white:#fff;
}
*{margin:0;padding:0;box-sizing:border-box}
html,body{width:780px;height:1200px;overflow:hidden}
body{position:relative;background:var(--white);font-family:"Arimo",Arial,sans-serif;color:var(--body-text)}
.abs{position:absolute}

.top-nav{left:0;top:0;width:780px;height:24px;background:var(--nav)}
.top-nav ul{list-style:none;position:absolute;right:0;top:0;display:flex;height:24px}
.top-nav li{font-size:10px;color:var(--white);padding:0 12px;line-height:24px;letter-spacing:.2px}
.top-nav li.active{background:var(--nav-active);color:#e9f3e3;padding:0 13px}

.header-band{left:0;top:24px;width:780px;height:183px;background:var(--band)}
.header-fade{left:0;top:207px;width:780px;height:115px;background:linear-gradient(#ececec,#fff)}

.phone{right:18px;top:38px;display:flex;align-items:center;gap:6px;color:var(--white);font-weight:700;font-size:16px}

.brand-art{left:17px;top:69px;width:207px;height:198px;border-radius:6px;background:linear-gradient(180deg,#ffffff 0%,#f2f2f2 50%,#cfe3da 78%,#c9b39e 100%)}
.brand-name{left:40px;top:116px;width:142px;text-align:right;font-weight:700;font-size:14px;line-height:17px;color:#8a9a7e}

.slider{left:247px;top:74px;width:516px;height:248px;border:6px solid var(--frame);border-radius:10px;overflow:hidden}
.slider .photo{position:absolute;inset:0;background:linear-gradient(160deg,#6f8fa8 0%,#5f7a3c 25%,#d9d2c0 45%,#4a6430 65%,#e6ddc8 85%,#6c7a4a 100%)}
.slider .arrow{position:absolute;top:120px;width:22px;height:22px;background:rgba(30,30,30,.75);border-radius:2px}
.slider .arrow.prev{left:6px}
.slider .arrow.next{right:6px}
.slider .dots{position:absolute;right:10px;bottom:10px;display:flex;gap:4px}
.slider .dots span{width:11px;height:11px;border-radius:50%;background:#a9cf95}
.slider .dots span.on{background:#e8f2e2}

.welcome-title{left:12px;top:354px;font-size:16.5px;font-weight:700;color:var(--green-text)}
.rule{height:1px;background:var(--rule)}
.welcome-rule{left:12px;top:378px;width:750px}
.welcome-text{left:13px;top:394px;width:735px;font-size:9.5px;line-height:16.5px;color:var(--body-text)}

.panel{top:556px;width:221px;height:229px;border-radius:8px;border:1px solid #bcd8ae;background:linear-gradient(var(--box-top),var(--box-bottom));box-shadow:0 14px 12px -10px rgba(0,0,0,.08)}
.panel-tab{top:544px;height:44px;background:var(--tab);color:var(--white);font-size:16px;font-weight:700;padding:10px 0 0 16px;border-radius:0 0 6px 6px}
.panel-tab::before,.panel-tab::after{content:"";position:absolute;top:0;border-bottom:12px solid var(--tab-dark)}
.panel-tab::before{left:-6px;border-left:6px solid transparent}
.panel-tab::after{right:-6px;border-right:6px solid transparent}
.services-panel{left:12px}
.about-panel{left:282px}
.testimonials-panel{left:543px}

.service-list{left:22px;top:596px;width:200px;list-style:none}
.service-list li{display:flex;align-items:center;gap:10px;height:21.4px;font-size:11px;font-weight:700;color:var(--white);border-bottom:1px dotted rgba(255,255,255,.7);padding-left:6px}
.service-list li:last-child{border-bottom:none}

.about-text{left:297px;top:599px;width:195px;font-size:11px;line-height:13.1px;color:var(--white)}

.testimonial{left:556px;width:190px}
.testimonial .mark{position:absolute;font-size:52px;line-height:40px;color:#8aa37a;font-family:Georgia,serif;opacity:.7}
.testimonial p{margin-left:34px;font-size:9px;line-height:11px;color:var(--dark-text)}
.testimonial .name{margin-left:37px;margin-top:6px;font-size:12.5px;color:var(--dark-text)}
.testimonial .close{left:74px;top:48px;color:#9bb48b;opacity:.6}

.clients-title{left:21px;top:846px;font-size:16.5px;font-weight:700;color:var(--green-text)}
.clients-rule{left:18px;top:870px;width:746px}
.client-logos{left:19px;top:887px;display:flex;gap:15px}
.client-logos div{width:111px;height:102px;border:5px solid var(--logo-border);display:flex;align-items:center;justify-content:center;font-size:16px;font-weight:700;color:var(--logo-text)}

.footer-scene{left:0;top:1010px;width:780px;height:190px;background:linear-gradient(180deg,#ffffff 0%,var(--footer-top) 40%,var(--footer-bottom) 100%)}
.copyright{right:17px;top:1145px;font-size:9.5px;color:#4f6b44}
</style>
</head>
<body>
<nav class="top-nav abs">
  <ul>
    <li>HOME</li><li>ABOUT US</li><li class="active">OUR SERVICES</li><li>GET A QUOTE</li><li>CONTACT US</li>
  </ul>
</nav>
<div class="header-band abs"></div>
<div class="header-fade abs"></div>

<div class="phone abs">
  <svg width="19" height="19" viewBox="0 0 20 20" aria-hidden="true"><circle cx="10" cy="10" r="8.8" fill="none" stroke="#fff" stroke-width="1.6"/><path d="M7.2 5.5l1.6 2.4-1 1.1c.5 1.3 1.4 2.2 2.7 2.8l1.1-1 2.3 1.6-.9 1.9c-3.5-.3-6.3-3.1-6.7-6.7z" fill="#fff"/></svg>
  <span>08 5550 2718</span>
</div>

<div class="brand-art abs" role="img" aria-label="Brand illustration: arborist character beside a tree under a cloud"></div>
<div class="brand-name abs">HOLLOW RIDGE<br>GROUNDCARE</div>

<div class="slider abs">
  <div class="photo" role="img" aria-label="Photo looking up at tall pale eucalyptus trunks and green canopy"></div>
  <div class="arrow prev"><svg width="22" height="22" viewBox="0 0 22 22" aria-hidden="true"><path d="M13 6l-5 5 5 5" fill="none" stroke="#fff" stroke-width="2"/></svg></div>
  <div class="arrow next"><svg width="22" height="22" viewBox="0 0 22 22" aria-hidden="true"><path d="M9 6l5 5-5 5" fill="none" stroke="#fff" stroke-width="2"/></svg></div>
  <div class="dots"><span></span><span></span><span class="on"></span><span></span><span></span></div>
</div>

<h1 class="welcome-title abs">Welcome at Hollow Ridge Groundcare</h1>
<div class="welcome-rule rule abs"></div>
<p class="welcome-text abs">Lorem ipsum dolor sit amet, consectetuer adipiscing elit, sed diam nonummy nibh euismod tincidunt ut laoreet dolore magna aliquam erat volutpat. Ut wisi enim ad minim veniam, quis nostrud exerci tation ullamcorper suscipit lobortis nisl ut aliquip ex ea commodo consequat. Duis autem vel eum iriure dolor in hendrerit in vulputate velit esse molestie consequat, vel illum dolore eu feugiat nulla facilisis at vero eros et accumsan et iusto odio dignissim qui blandit praesent luptatum zzril delenit augue duis dolore te feugait nulla facilisi. Nam liber tempor cum soluta nobis eleifend option congue nihil imperdiet doming id quod mazim placerat facer possim assum. Typi non habent claritatem insitam; est usus legentis in iis qui facit eorum claritatem. Investigationes demonstraverunt lectores legere me lius quod ii legunt saepius. Claritas est etiam processus dynamicus, qui sequitur mutationem consuetudium lectorum. Mirum est notare quam littera gothica, quam nunc putamus parum claram, anteposuerit litterarum formas humanitatis per seacula quarta decima et quinta decima. Eodem modo typi, qui nunc nobis videntur parum clari, fiant sollemnes in futurum.</p>

<div class="panel services-panel abs"></div>
<div class="panel-tab abs" style="left:42px;width:157px">Our Services</div>
<ul class="service-list abs">
  <li><svg width="13" height="13" viewBox="0 0 14 14" aria-hidden="true"><circle cx="7" cy="7" r="7" fill="#fff"/><path d="M3.8 7.2l2.2 2.2 4.2-4.4" fill="none" stroke="#79a966" stroke-width="1.8"/></svg>Diagnosis</li>
  <li><svg width="13" height="13" viewBox="0 0 14 14" aria-hidden="true"><circle cx="7" cy="7" r="7" fill="#fff"/><path d="M3.8 7.2l2.2 2.2 4.2-4.4" fill="none" stroke="#79a966" stroke-width="1.8"/></svg>Treatment</li>
  <li><svg width="13" height="13" viewBox="0 0 14 14" aria-hidden="true"><circle cx="7" cy="7" r="7" fill="#fff"/><path d="M3.8 7.2l2.2 2.2 4.2-4.4" fill="none" stroke="#79a966" stroke-width="1.8"/></svg>Purning</li>
  <li><svg width="13" height="13" viewBox="0 0 14 14" aria-hidden="true"><circle cx="7" cy="7" r="7" fill="#fff"/><path d="M3.8 7.2l2.2 2.2 4.2-4.4" fill="none" stroke="#79a966" stroke-width="1.8"/></svg>Tree Removal</li>
  <li><svg width="13" height="13" viewBox="0 0 14 14" aria-hidden="true"><circle cx="7" cy="7" r="7" fill="#fff"/><path d="M3.8 7.2l2.2 2.2 4.2-4.4" fill="none" stroke="#79a966" stroke-width="1.8"/></svg>Stump Removal</li>
  <li><svg width="13" height="13" viewBox="0 0 14 14" aria-hidden="true"><circle cx="7" cy="7" r="7" fill="#fff"/><path d="M3.8 7.2l2.2 2.2 4.2-4.4" fill="none" stroke="#79a966" stroke-width="1.8"/></svg>Cabling &amp; Bracing</li>
  <li><svg width="13" height="13" viewBox="0 0 14 14" aria-hidden="true"><circle cx="7" cy="7" r="7" fill="#fff"/><path d="M3.8 7.2l2.2 2.2 4.2-4.4" fill="none" stroke="#79a966" stroke-width="1.8"/></svg>Arborist Consults</li>
  <li><svg width="13" height="13" viewBox="0 0 14 14" aria-hidden="true"><circle cx="7" cy="7" r="7" fill="#fff"/><path d="M3.8 7.2l2.2 2.2 4.2-4.4" fill="none" stroke="#79a966" stroke-width="1.8"/></svg>Tree Protection</li>
</ul>

<div class="panel about-panel abs"></div>
<div class="panel-tab abs" style="left:312px;width:151px">About Us</div>
<p class="about-text abs">Lorem ipsum dolor sit amet, consectetuer adipiscing elit, sed diam nonummy nibh euismod tincidunt ut laoreet dolore magna aliquam erat volutpat. Ut wisi enim ad minim veniam, quis nostrud exerci tation ullamcorper suscipit lobortis nisl ut aliquip ex ea commodo consequat. Duis autem vel eum iriure dolor in hendrerit in vulputate velit esse molestie consequat, vel illum dolore eu feugiat per seacula quarta decima et quinta decima.</p>

<div class="panel testimonials-panel abs"></div>
<div class="panel-tab abs" style="left:578px;width:146px">Testimonials</div>
<div class="testimonial abs" style="top:596px">
  <span class="mark" style="left:0;top:0">&ldquo;</span>
  <span class="mark close">&rdquo;</span>
  <p>Lorem ipsum dolor sit amet, consectetuer adipiscing elit, sed diam nonummy nibh euismod tincidunt ut laoreet dolore magna aliquam erat volutpat.</p>
  <div class="name">Tessa</div>
</div>
<div class="testimonial abs" style="top:685px">
  <span class="mark" style="left:0;top:0">&ldquo;</span>
  <span class="mark close">&rdquo;</span>
  <p>Lorem ipsum dolor sit amet, consectetuer adipiscing elit, sed diam nonummy nibh euismod tincidunt ut laoreet dolore magna aliquam erat volutpat.</p>
  <div class="name">Tessa</div>
</div>

<h2 class="clients-title abs">Our Clients</h2>
<div class="clients-rule rule abs"></div>
<div class="client-logos abs">
  <div>Logo</div><div>Logo</div><div>Logo</div><div>Logo</div><div>Logo</div><div>Logo</div>
</div>

<div class="footer-scene abs" role="img" aria-label="Footer illustration: rolling green hills with cartoon trees"></div>
<div class="copyright abs">Copyright 2013 www.hollowridgegroundcare.example. All right reserved.</div>
</body>
</html>
```